Will you marry me post card

I am just looking for a postcard to send my partner that will ask him to marry me.
I plan on creating about 200 of them and mailing them all at once so that he gets them all on the same day.
They should all be similar or could have a few different options.
I would like it simple, elegant, clean and crisp. No images, just text or icons

My only requirement is the text, "will you marry me?" in all lowercase -- any fonts, can be big, small, varying sizes, repeated, whole card, tiny space, don't care...just amazing design. BUT SIMPLE!

```html
<!DOCTYPE html>
<html lang="en">
<head>
<meta charset="utf-8">
<title>will you marry me? postcards</title>
<link rel="stylesheet" href="https://fonts.googleapis.com/css2?family=Pacifico&display=swap">
<style>
  :root {
    --canvas-bg: #ffffff;
    --sky-blue: #42a8c6;
    --butterfly-blue: #8dd0ea;
    --leaf-green: #7cc36a;
    --leaf-yellow: #f4ea47;
    --ink-white: #ffffff;
  }
  html, body {
    margin: 0;
    padding: 0;
    width: 1200px;
    height: 761px;
    overflow: hidden;
    background: var(--canvas-bg);
  }
  .canvas {
    position: relative;
    width: 1200px;
    height: 761px;
  }
  .postcard {
    position: absolute;
    top: 18px;
    width: 559px;
    height: 722px;
  }
  .postcard--blue { left: 27px; }
  .postcard--green { left: 615px; }
  .postcard svg { display: block; width: 100%; height: 100%; }
  .script {
    font-family: "Pacifico", "Brush Script MT", cursive;
    fill: var(--ink-white);
  }
</style>
</head>
<body>
<main class="canvas">

  <section class="postcard postcard--blue">
    <svg viewBox="0 0 559 722" xmlns="http://www.w3.org/2000/svg">
      <defs>
        <radialGradient id="butterfly-glow" cx="50%" cy="50%" r="50%">
          <stop offset="0%" stop-color="#8dd0ea" stop-opacity="0.9"/>
          <stop offset="100%" stop-color="#8dd0ea" stop-opacity="0"/>
        </radialGradient>
      </defs>
      <rect class="card-bg" width="559" height="722" fill="var(--sky-blue)"/>
      <g class="butterflies">
        <ellipse role="img" aria-label="small pale blue butterfly silhouette" cx="440" cy="160" rx="50" ry="50" fill="url(#butterfly-glow)"/>
        <ellipse role="img" aria-label="small pale blue butterfly silhouette" cx="434" cy="320" rx="31" ry="42" fill="url(#butterfly-glow)"/>
        <ellipse role="img" aria-label="large pale blue butterfly silhouette" cx="150" cy="532" rx="89" ry="88" fill="url(#butterfly-glow)"/>
      </g>
      <g class="proposal">
        <text class="script" x="125" y="195" font-size="96">will</text>
        <text class="script" x="64" y="294" font-size="96">you</text>
        <text class="script" x="125" y="415" font-size="96">mary</text>
        <text class="script" x="269" y="529" font-size="96">me?</text>
      </g>
    </svg>
  </section>

  <section class="postcard postcard--green">
    <svg viewBox="0 0 559 722" xmlns="http://www.w3.org/2000/svg">
      <defs>
        <linearGradient id="leaf-fade-top" x1="0" y1="0" x2="1" y2="1">
          <stop offset="0%" stop-color="#f4ea47" stop-opacity="0.85"/>
          <stop offset="100%" stop-color="#f4ea47" stop-opacity="0.35"/>
        </linearGradient>
        <linearGradient id="leaf-fade-bottom" x1="1" y1="0" x2="0" y2="1">
          <stop offset="0%" stop-color="#f4ea47" stop-opacity="0.85"/>
          <stop offset="100%" stop-color="#f4ea47" stop-opacity="0.35"/>
        </linearGradient>
      </defs>
      <rect class="card-bg" width="559" height="722" fill="var(--leaf-green)"/>
      <rect class="branch branch--top" role="img" aria-label="yellow leafy branch reaching across the top of the card" x="0" y="10" width="559" height="340" rx="170" fill="url(#leaf-fade-top)"/>
      <rect class="branch branch--bottom" role="img" aria-label="yellow leafy branch rising from the lower right corner" x="215" y="470" width="344" height="225" rx="110" fill="url(#leaf-fade-bottom)"/>
      <g class="proposal">
        <text class="script" x="46" y="362" font-size="44">will you</text>
        <text class="script" x="76" y="432" font-size="96">marry</text>
        <text class="script" x="114" y="508" font-size="96">me</text>
        <text class="script" x="150" y="612" font-size="88">?</text>
      </g>
    </svg>
  </section>

</main>
</body>
</html>
```